Clara Whitfield: Adult Models Flyer

We need an attractive flyer design to promote our adult modeling agency and recruit models to our business. We hire beautiful, young women and couples to be on a live adult camshow. We would like to highlight the following features of this job position:

-Pays $100/hour
-Set your own schedule
-Have fun and get paid
-Sign up at cwadultmodels.example

The theme should be similar to the website (hot pink and white). We are putting these flyers around college campuses and nightclubs.
Updates

Just uploaded a couple pics of me and my new model that might work well on the flyer(:

Target Market(s)

Our audience is attractive, young women (college students, baristas, waitresses etc.)

Industry/Entity Type

College

Requirements
Must have
• A picture of Clara Whitfield. Perhaps a long body shot on the side or just her face somewhere. Pictures can be found here: https://chirpnet.example/WhitfieldClara
and here: http://picvue.example/whitfieldclara

A visible and bold area featuring: "$100/hour"

```html
<!DOCTYPE html>
<html lang="en">
<head>
<meta charset="utf-8">
<title>Clara Whitfield – Adult Models Flyer</title>
<link rel="stylesheet" href="https://fonts.googleapis.com/css2?family=Open+Sans:wght@400;600;700;800&family=Parisienne&display=swap">
<style>
  :root {
    --page-bg: #ececec;
    --paper: #ffffff;
    --paper-tint: #fbe7f1;
    --hot-pink: #e2378e;
    --pink-deep: #c81f75;
    --pink-rim: #f7a8cd;
    --pink-soft: #f4bcd8;
    --ink-white: #ffffff;
    --shadow: rgba(90, 20, 55, 0.28);
    --photo-warm: #c79a78;
    --photo-dark: #5a4032;
    --frame-grey: #e6e6e6;
  }
  * { box-sizing: border-box; margin: 0; padding: 0; }
  html, body {
    width: 960px; height: 1200px; overflow: hidden;
    background: var(--page-bg);
    font-family: "Open Sans", Arial, sans-serif;
  }
  .canvas { position: relative; width: 960px; height: 1200px; }

  .flyer {
    position: absolute; left: 105px; top: 21px;
    width: 750px; height: 1158px;
    background: var(--paper);
    box-shadow: 0 10px 40px rgba(0,0,0,0.18);
    overflow: hidden;
  }
  .flyer-backdrop {
    position: absolute; left: 0; top: 0; width: 750px; height: 1028px;
    background: var(--paper-tint);
  }

  .brand-mark {
    position: absolute; left: 240px; top: 38px; width: 300px; height: 170px;
    display: flex; flex-direction: column; align-items: center; justify-content: center;
  }
  .brand-row { display: flex; align-items: center; gap: 12px; }
  .brand-dot { width: 34px; height: 34px; border-radius: 50%; background: var(--hot-pink); }
  .brand-name { font-size: 34px; font-weight: 700; color: var(--hot-pink); letter-spacing: 0.5px; }
  .brand-tag { margin-top: 6px; font-size: 11px; font-weight: 600; letter-spacing: 3px; color: #333; }

  .webcam { position: absolute; left: 576px; top: 186px; width: 48px; height: 58px; }

  .photo-frame {
    position: absolute; left: 78px; top: 207px; width: 591px; height: 336px;
    background: var(--paper); border-radius: 8px;
    box-shadow: 0 4px 16px rgba(0,0,0,0.22); border: 2px solid var(--frame-grey);
  }
  .photo-strip {
    position: absolute; left: 16px; top: 21px; width: 555px; height: 303px;
    background: linear-gradient(90deg, var(--photo-dark) 0%, var(--photo-warm) 25%, #3c3030 45%, #e7b9a0 62%, #f08cb8 78%, #d9a98a 100%);
  }

  .ribbon {
    position: absolute; display: flex; align-items: center; justify-content: center;
    background: var(--hot-pink); color: var(--ink-white);
    border: 4px solid var(--pink-rim); border-radius: 6px;
    box-shadow: 0 8px 14px var(--shadow);
  }
  .ribbon-pay { left: 25px; top: 547px; width: 698px; height: 105px; z-index: 3; }
  .ribbon-schedule { left: 67px; top: 657px; width: 614px; height: 83px; z-index: 2; }
  .ribbon-fun { left: 107px; top: 744px; width: 537px; height: 83px; z-index: 1; }
  .pay-text {
    font-size: 47px; font-weight: 800; letter-spacing: 0.5px;
    text-shadow: 2px 3px 0 var(--pink-deep), 0 0 2px rgba(0,0,0,0.3);
    color: #fbeef4;
  }
  .perk-text { font-size: 34px; font-weight: 400; letter-spacing: 0.3px; }
  .kiss {
    position: absolute; top: 22px; width: 64px; height: 52px;
    border-radius: 50%; background: var(--ink-white); opacity: 0.92;
  }
  .kiss-left { left: 32px; }
  .kiss-right { right: 32px; }

  .motto {
    position: absolute; left: 100px; top: 878px; width: 550px;
    text-align: center; font-family: "Parisienne", cursive;
    font-size: 43px; line-height: 56px; color: var(--hot-pink);
  }

  .footer {
    position: absolute; left: 0; top: 1028px; width: 750px; height: 130px;
    background: var(--paper);
  }
  .footer-brand {
    position: absolute; left: 50px; top: 40px;
    display: flex; align-items: center; gap: 10px;
  }
  .footer-dot { width: 28px; height: 28px; border-radius: 50%; background: var(--hot-pink); }
  .footer-name { font-size: 22px; font-weight: 600; color: var(--hot-pink); }
  .signup { position: absolute; right: 57px; top: 40px; text-align: center; }
  .signup-label { font-size: 20px; font-weight: 400; color: var(--pink-deep); letter-spacing: 0.3px; }
  .signup-url { font-size: 23px; font-weight: 700; color: var(--hot-pink); letter-spacing: 0.2px; }
</style>
</head>
<body>
<main class="canvas">
  <article class="flyer">
    <div class="flyer-backdrop" role="img" aria-label="Pale pink background pattern of repeated monogram motifs"></div>

    <header class="brand-mark">
      <div class="brand-row">
        <span class="brand-dot"></span>
        <span class="brand-name">Clara Whitfield</span>
      </div>
      <span class="brand-tag">ADULT MODELS</span>
    </header>

    <svg class="webcam" viewBox="0 0 48 58" aria-hidden="true">
      <rect x="14" y="40" width="20" height="16" rx="4" fill="#f2f2f2" stroke="#cfcfcf"/>
      <circle cx="24" cy="22" r="20" fill="#f7f7f7" stroke="#cfcfcf" stroke-width="2"/>
      <circle cx="24" cy="22" r="9" fill="#2b2b3a"/>
      <circle cx="21" cy="19" r="2.5" fill="#8c8cb0"/>
    </svg>

    <section class="photo-frame">
      <div class="photo-strip" role="img" aria-label="Collage of photos of the models in casual outfits and swimwear"></div>
    </section>

    <div class="ribbon ribbon-pay">
      <span class="kiss kiss-left" role="img" aria-label="Lipstick kiss mark"></span>
      <span class="pay-text">PAYS $100/HOUR</span>
      <span class="kiss kiss-right" role="img" aria-label="Lipstick kiss mark"></span>
    </div>
    <div class="ribbon ribbon-schedule"><span class="perk-text">SET YOUR OWN SCHEDULE</span></div>
    <div class="ribbon ribbon-fun"><span class="perk-text">HAVE FUN AND GET PAID</span></div>

    <p class="motto">“ Life doesnt have to be hard, it can be fun and easy! ”</p>

    <footer class="footer">
      <div class="footer-brand">
        <span class="footer-dot"></span>
        <span class="footer-name">Clara Whitfield</span>
      </div>
      <div class="signup">
        <div class="signup-label">SIGN UP AT</div>
        <div class="signup-url">WWW.CWADULTMODELS.EXAMPLE</div>
      </div>
    </footer>
  </article>
</main>
</body>
</html>
```